Local Roofing/Construction company business needs new biz card design

We need a new business card design, current cards are from the start of this operation and generic at best. We are a local Construction Company (General Contractor) with a majority of our work originating from insurance claims-exterior finish work is the main focus (Roofs-Siding-Gutters etc). Heavily involved with homeowners and the low ball offers they receive from insurance company's after a insurable event takes place. I have attached some of our original logo file(s) below.

```html
<!DOCTYPE html>
<html lang="en">
<head>
<meta charset="UTF-8">
<title>Stoneline Construction – Business Card</title>
<link href="https://fonts.googleapis.com/css2?family=Montserrat:wght@500;700&family=Open+Sans:wght@400&display=swap" rel="stylesheet">
<style>
  :root {
    --bg: #d4d7d8;
    --card: #fbfbfb;
    --green: #1f9a3e;
    --green-line: #4cb465;
    --ink: #2b2b2b;
    --muted: #555a5c;
  }
  * { box-sizing: border-box; margin: 0; padding: 0; }
  html, body { width: 1200px; height: 829px; overflow: hidden; }
  body {
    background: var(--bg);
    font-family: "Open Sans", Arial, sans-serif;
    display: flex;
    align-items: center;
    justify-content: center;
    gap: 48px;
  }
  .card {
    width: 540px;
    height: 309px;
    background: var(--card);
    border-bottom: 4px solid var(--green);
    box-shadow: 0 14px 28px rgba(0,0,0,0.18);
    position: relative;
  }
  /* Front */
  .card-front .person { position: absolute; left: 34px; top: 42px; }
  .person-name {
    font-family: "Montserrat", Arial, sans-serif;
    font-weight: 700;
    font-size: 21px;
    letter-spacing: 1px;
    color: var(--green);
    text-transform: uppercase;
  }
  .person-title { font-size: 13px; color: var(--muted); margin-top: 2px; }
  .divider {
    position: absolute; left: 34px; right: 34px; top: 108px;
    height: 1px; background: var(--green-line);
  }
  .contacts { position: absolute; left: 34px; top: 124px; list-style: none; }
  .contacts li {
    display: flex; align-items: center; gap: 9px;
    font-size: 13.5px; color: var(--ink); line-height: 25px;
  }
  .contacts svg { width: 11px; height: 11px; fill: var(--green); flex: none; }
  .brand {
    display: flex; align-items: center; gap: 10px;
    font-family: "Montserrat", Arial, sans-serif;
    font-weight: 700; color: var(--green);
    text-transform: uppercase; letter-spacing: 0.5px;
  }
  .brand-mark { background: var(--green); flex: none; }
  .card-front .brand { position: absolute; right: 34px; top: 42px; font-size: 15px; }
  .card-front .brand-mark { width: 14px; height: 14px; }
  .address {
    position: absolute; right: 34px; bottom: 30px;
    text-align: right; font-size: 13.5px; line-height: 21px; color: var(--ink);
  }
  /* Back */
  .card-back { display: flex; align-items: center; justify-content: center; }
  .card-back .brand { font-size: 22px; gap: 14px; }
  .card-back .brand-mark { width: 22px; height: 22px; }
</style>
</head>
<body>
  <section class="card card-front">
    <div class="person">
      <h1 class="person-name">Dylan Marsh</h1>
      <p class="person-title">Managing Director</p>
    </div>
    <div class="brand"><span class="brand-mark"></span>Stoneline Construction</div>
    <div class="divider"></div>
    <ul class="contacts">
      <li><svg viewBox="0 0 24 24"><path d="M6.6 10.8a15 15 0 0 0 6.6 6.6l2.2-2.2a1 1 0 0 1 1-.25 11.4 11.4 0 0 0 3.6.57 1 1 0 0 1 1 1V20a1 1 0 0 1-1 1A17 17 0 0 1 3 4a1 1 0 0 1 1-1h3.5a1 1 0 0 1 1 1c0 1.25.2 2.45.57 3.57a1 1 0 0 1-.25 1z"/></svg>0412 555 019</li>
      <li><svg viewBox="0 0 24 24"><path d="M2 5h20v14H2z M2 5l10 8 10-8" /></svg>info@stonelinebuild.com</li>
      <li><svg viewBox="0 0 24 24"><circle cx="12" cy="12" r="10"/></svg>www.stonelinebuild.com</li>
    </ul>
    <address class="address" style="font-style:normal">
      1450 Harlow Avenue<br>
      Ashford County Name 5120
    </address>
  </section>

  <section class="card card-back">
    <div class="brand"><span class="brand-mark"></span>Stoneline Construction</div>
  </section>
</body>
</html>
```